Premium Lawn fertiliser packaging - Looking for long term designer

*Update at bottom
I need a carefully considered, bold and professional packaging design for my new premium lawn fertiliser product. This contest is for a detailed front of the stand-up pouch packaging and once I’ve chosen a winner, they’ll be asked to create the layout for the back that links to the front as well. I have a full range of additional products that will also need designs and so I'm looking for someone who can do a great job here and who we can work with long term.

The front should include our logo for Pemberly Turf Supply Direct and be titled “Bloom Vigor Max” "Professional Lawn Fertiliser". The spring fertiliser tag line is "Awaken your lawn: Lush Greening, Lasting Health".
Beneath it, it then needs to include some important usage information and the key benefits along with some suitable graphic.

Key information to include:

Apply March - June
Treats 35-50 m2
16-3-8
+2%MgO + 1% Fe + 2.9% CaO (this is the chemical makeup of the fertiliser and needs to be fairly prominent. If you look at other professional fertiliser packaging, you'll see how it needs to compare).

Key features:
Premium fertiliser, used by professionals
Advanced greening with micro-nutrient complex
Dual action Nitrogen: Instant green boost & continuous feed for 3 months
Child & pet safe

Our brand colours are purple and green. Purple = #592999, Green = 3cb64a / 81d742 / 4d9d44

I think these colours look great against a white background.

Please make sure you look at our website as well to get an idea of our brand: www.pemberlyturfsupply.co.uk

To help, I've attached images of competitors fertiliser packaging that I like the look of. I'm not looking for you to copy but just see what type of thing appeals to me, the standard I'm expecting and what I need to compete against....

In addition, I have also attached some potential images you may wish to try using in your design, although please feel free to use your own if you have something better. For the moment, the images are 'preview' images, but once I decide on a design and we agree on the correct image, I will download and send over a fully licensed version.

*** Update*** When submitting your design, can you submit it in 2 formats: The first as a fully printed custom stand-up pouch and the second as a full-size label stuck onto a standup pouch (whatever colour you think is right for your design - choose white if you are not sure). To explain, I've just discovered we won't be able to get full custom bags printed in time for the first run and so we will have to opt for the design to be printed on labels and fixed onto bags. I therefore need to choose a design that works in both formats as both a label on a standup pouch as well as a fully printed pouch. Many thanks.

Target Market(s)

Domestic home-owners

Industry/Entity Type

Lawn care. NOT AGRICULTURE OR FARMING

Font styles to use
Sans Serif

Requirements
Must have
• Presented in 2 formats - see update at bottom of description
Nice to have
• I quite like designs against a white background, although I’m open to other ideas as well.
Should not have
• Please do not include any people or faces in the design. The text should be solid in colour, so no graduated colour fill in the text or outline text. Please avoid over-busy or cluttered designs.

```html
<!DOCTYPE html>
<html lang="en">
<head>
<meta charset="UTF-8">
<title>Bloom Vigor Max – Professional Lawn Fertiliser</title>
<link href="https://fonts.googleapis.com/css2?family=Oswald:wght@700&family=Poppins:ital,wght@0,500;0,600;0,700;1,500&family=Roboto:wght@400;500;700&display=swap" rel="stylesheet">
<style>
  :root {
    --canvas: #e6e7e9;
    --white: #ffffff;
    --purple: #592999;
    --purple-deep: #4a1f86;
    --green: #3cb64a;
    --green-light: #81d742;
    --green-dark: #4d9d44;
    --green-bag: #1f9a3a;
    --yellow: #f5e400;
    --brand-text: #2f7a2a;
  }
  * { box-sizing: border-box; margin: 0; padding: 0; }
  html, body {
    width: 1200px; height: 1200px; overflow: hidden;
    background: var(--canvas);
  }
  .pouch {
    position: absolute; left: 360px; top: 170px;
    width: 480px; height: 860px;
    background: var(--white);
    display: flex; flex-direction: column;
    overflow: hidden;
  }
  .brand {
    height: 235px;
    display: flex; flex-direction: column; align-items: center; justify-content: center;
    gap: 14px; padding-top: 40px;
  }
  .brand-mark {
    width: 40px; height: 40px; border-radius: 50%;
    background: var(--green-light);
  }
  .brand-name {
    font-family: "Poppins", sans-serif; font-weight: 600;
    font-size: 30px; line-height: 1.1; text-align: center;
    color: var(--brand-text);
  }
  .grass-strip {
    height: 65px;
    background: linear-gradient(to bottom, var(--white) 0%, var(--green-light) 45%, var(--green-dark) 100%);
  }
  .title-band {
    height: 150px; background: var(--purple);
    display: flex; flex-direction: column; align-items: center;
    padding-top: 20px; position: relative;
  }
  .product-name {
    font-family: "Oswald", sans-serif; font-weight: 700;
    font-size: 54px; line-height: 1; letter-spacing: 0.5px;
    color: var(--white); text-transform: uppercase;
  }
  .product-type {
    font-family: "Poppins", sans-serif; font-weight: 700;
    font-size: 22px; line-height: 1.2; margin-top: 8px;
    color: var(--yellow);
  }
  .tagline {
    position: absolute; bottom: -12px; left: 50%; transform: translateX(-50%);
    background: var(--green-bag); color: var(--white);
    font-family: "Poppins", sans-serif; font-style: italic; font-weight: 500;
    font-size: 12.5px; white-space: nowrap;
    padding: 4px 20px; border-radius: 3px; z-index: 2;
  }
  .hero {
    height: 270px; position: relative;
  }
  .hero-scene {
    position: absolute; inset: 0;
    background: linear-gradient(to bottom, #e9eff2 0%, #cfdcc8 35%, #8fa38a 52%, #7fc247 68%, #5fb234 100%);
  }
  .usage-box {
    position: absolute; left: 50%; bottom: 12px; transform: translateX(-50%);
    width: 134px; padding: 5px 6px 4px;
    background: var(--purple); border-radius: 4px;
    color: var(--white); text-align: center;
  }
  .usage-season {
    font-family: "Roboto", sans-serif; font-weight: 500; font-size: 9.5px;
  }
  .usage-coverage {
    font-family: "Poppins", sans-serif; font-weight: 700; font-size: 22px; line-height: 1.15;
  }
  .usage-analysis {
    font-family: "Roboto", sans-serif; font-weight: 500; font-size: 5.5px;
  }
  .benefits-panel {
    flex: 1; background: var(--green-bag);
    display: flex; flex-direction: column; align-items: center;
    padding-top: 12px; color: var(--white);
  }
  .benefits {
    list-style: none; text-align: center;
    font-family: "Roboto", sans-serif; font-size: 9.5px; line-height: 1.55;
  }
  .benefits li::before { content: "\2713\00a0"; }
  .net-weight {
    margin-top: 20px;
    font-family: "Roboto", sans-serif; font-weight: 700; font-size: 17px;
  }
</style>
</head>
<body>
  <main class="pouch">
    <header class="brand">
      <div class="brand-mark"></div>
      <div class="brand-name">Pemberly Turf<br>Supply Direct</div>
    </header>

    <div class="grass-strip" role="img" aria-label="Row of fresh green grass blades"></div>

    <section class="title-band">
      <h1 class="product-name">Bloom Vigor Max</h1>
      <p class="product-type">Professional Lawn Fertiliser</p>
      <p class="tagline">Awaken your Lawn: Lush Greening, Lasting Health</p>
    </section>

    <section class="hero">
      <div class="hero-scene" role="img" aria-label="Photograph of a large family house with landscaped borders and a lush green front lawn"></div>
      <div class="usage-box">
        <div class="usage-season">APPLY MARCH - JUNE</div>
        <div class="usage-coverage">35-50 M2</div>
        <div class="usage-analysis">16 - 3 - 8 + 2% MgO + 1% Fe + 2.9% CaO</div>
      </div>
    </section>

    <section class="benefits-panel">
      <ul class="benefits">
        <li>Premium fertiliser, used by professionals</li>
        <li>Advanced greening with micro-nutrient complex</li>
        <li>Dual action Nitrogen: Instant green boost &amp; continuous feed for 3 months</li>
        <li>Child &amp; pet safe</li>
      </ul>
      <div class="net-weight">10KG</div>
    </section>
  </main>
</body>
</html>
```